Presentation Flyer for Married Couple at night separate business owners by day

I would like a flyer to use to advertise free presentations put on by husband and I. I (Renata Volkhaven) am an estate planning attorney that works for PWR Law. My husband (Dan Volkhaven) is a financial planner that works for Quelmora Financial Planning. Would love it to be funny but serious. At night we are a married couple of 4 children, by day we individually work with people helping them protect their assets and their families.
Goal is for this to be used for multiple events.
Things to include: Food will be provided, Raffle for $500 off an Estate Plan Package
Topics to be covered in Seminar:
Estate & Financial Planning Essentials

Protect Your Future
Build a strong financial foundation with emergency funds, retirement planning, and smart investment strategies that match your goals.

Secure Your Legacy
Learn about wills, trusts, and powers of attorney - the essential documents everyone needs to protect their family's future.

Guard Your Assets
Understand the right insurance coverage to protect yourself and your loved ones, from life insurance to long-term care options.

Transfer Wealth Wisely
Discover tax-efficient strategies for passing assets to the next generation and making the most of your charitable giving.

```html
<!DOCTYPE html>
<html lang="en">
<head>
<meta charset="utf-8">
<title>Estate &amp; Financial Planning Seminar</title>
<link rel="stylesheet" href="https://fonts.googleapis.com/css2?family=Archivo:wght@700;800;900&family=Poppins:wght@300;400;600;700;800&display=swap">
<style>
  :root {
    --paper: #f4f4f4;
    --ink: #111111;
    --navy: #15213b;
    --band: #c4c3c1;
    --white: #ffffff;
    --teal: #1f6b6b;
  }
  * { margin: 0; padding: 0; box-sizing: border-box; }
  html, body { width: 848px; height: 1200px; overflow: hidden; background: var(--paper); }
  body { font-family: "Poppins", sans-serif; color: var(--ink); }
  .flyer { position: relative; width: 848px; height: 1200px; background: var(--paper); }

  .hero-photo {
    position: absolute; left: 422px; top: 0; width: 426px; height: 519px;
    background: linear-gradient(160deg, #b98466 0%, #9c6a52 35%, #3a4560 70%, #1f2740 100%);
  }

  .kicker {
    position: absolute; left: 85px; top: 144px; width: 330px;
    font-size: 19px; line-height: 21px; font-weight: 400; color: #2a2a2a;
  }
  .title-bar { position: absolute; left: 71px; top: 195px; width: 6px; height: 88px; background: var(--ink); }
  .title {
    position: absolute; left: 82px; top: 186px;
    font-family: "Archivo", sans-serif; font-size: 63px; line-height: 65px;
    letter-spacing: -1px; color: var(--ink);
  }
  .title .heavy { font-weight: 900; display: block; }
  .title .light { font-family: "Poppins", sans-serif; font-weight: 400; display: block; letter-spacing: -1px; margin-left: 0; }

  .tagline-band {
    position: absolute; left: 55px; top: 385px; width: 367px; height: 134px;
    background: var(--band); padding: 10px 0 0 28px;
  }
  .tagline { font-size: 22px; line-height: 24px; font-weight: 400; text-transform: uppercase; color: #1a1a1a; }
  .tagline-sub { margin-top: 11px; font-size: 14.5px; line-height: 17px; font-weight: 700; color: #111; }

  .details {
    position: absolute; left: 55px; top: 520px; width: 768px; height: 482px;
    background: var(--navy); color: var(--white);
  }
  .rule { position: absolute; left: 30px; width: 54px; height: 3px; background: var(--white); }
  .intro {
    position: absolute; left: 30px; top: 28px; width: 720px;
    font-size: 17px; line-height: 19.5px; font-weight: 400;
  }
  .intro strong { font-weight: 700; }
  .learn-heading {
    position: absolute; left: 29px; top: 119px;
    font-family: "Archivo", sans-serif; font-weight: 800; font-size: 22px;
  }
  .topic { position: absolute; width: 290px; }
  .topic h3 { font-family: "Archivo", sans-serif; font-weight: 800; font-size: 20px; line-height: 24px; margin-bottom: 4px; }
  .topic p { font-size: 16.5px; line-height: 20px; font-weight: 400; }

  .raffle {
    position: absolute; left: 616px; top: 132px; width: 148px; height: 154px;
    background: var(--white); color: var(--ink); border-radius: 12px;
    text-align: center; padding-top: 8px;
  }
  .raffle .win { font-size: 19px; line-height: 22px; }
  .raffle .amount { font-family: "Archivo", sans-serif; font-weight: 800; font-size: 42px; line-height: 44px; }
  .raffle .prize { font-size: 19px; line-height: 21px; }

  .food { position: absolute; left: 634px; top: 316px; width: 128px; text-align: center; }
  .food svg { display: block; margin: 0 auto; }
  .food p { font-weight: 800; font-size: 19.5px; line-height: 23px; margin-top: 6px; white-space: nowrap; margin-left: -10px; margin-right: -10px; }

  .venue-bar { position: absolute; left: 55px; top: 1038px; width: 5px; height: 23px; background: var(--ink); }
  .venue { position: absolute; left: 77px; top: 1035px; }
  .venue h4 { font-weight: 700; font-size: 23px; line-height: 28px; color: var(--ink); }
  .venue p { font-size: 20px; line-height: 23px; color: #2a2a2a; }

  .partner { position: absolute; display: flex; align-items: center; gap: 7px;
    font-family: "Poppins", sans-serif; font-weight: 600; color: var(--navy); }
  .partner .mark { width: 12px; height: 12px; background: var(--navy); }
  .partner-law { left: 512px; top: 1074px; font-size: 24px; }
  .partner-finance { left: 700px; top: 1076px; font-size: 21px; color: var(--teal); }
  .partner-finance .mark { background: var(--teal); border-radius: 50%; }
</style>
</head>
<body>
<main class="flyer">
  <div class="hero-photo" role="img" aria-label="Portrait of Renata and Dan Volkhaven smiling, seated in front of a brick wall"></div>

  <p class="kicker">A free seminar with Renata &amp; Dan Volkhaven</p>
  <div class="title-bar"></div>
  <h1 class="title">
    <span class="heavy">ESTATE &amp;</span>
    <span class="heavy">FINANCIAL</span>
    <span class="light">PLANNING:</span>
  </h1>

  <section class="tagline-band">
    <p class="tagline">Because your kids<br>don’t want your debt!</p>
    <p class="tagline-sub">By day, we help families protect their futures. By night, we’re just a married couple trying to keep up with four kids.</p>
  </section>

  <section class="details">
    <div class="rule" style="top:21px"></div>
    <p class="intro">Join <strong>Renata Volkhaven</strong>, an Estate Planning Attorney with <strong>PWR Law</strong>, and <strong>Dan Volkhaven</strong>, a Financial Planner with <strong>Quelmora Financial Planning</strong>, for a free, informative (and slightly entertaining) seminar on securing your family’s future.</p>

    <h2 class="learn-heading">WHAT YOU’LL LEARN:</h2>
    <div class="rule" style="top:156px"></div>

    <article class="topic" style="left:30px; top:170px;">
      <h3>Protect Your Future</h3>
      <p>Build a strong financial foundation with emergency funds, retirement planning, and smart investment strategies.</p>
    </article>
    <article class="topic" style="left:335px; top:170px;">
      <h3>Secure Your Legacy</h3>
      <p>Understand wills, trusts, and powers of attorney—the essential documents everyone needs.</p>
    </article>
    <article class="topic" style="left:30px; top:308px;">
      <h3>Guard Your Assets</h3>
      <p>Get the right insurance coverage to protect yourself and your loved ones, from life insurance to long-term care.</p>
    </article>
    <article class="topic" style="left:335px; top:308px;">
      <h3>Transfer Wealth Wisely</h3>
      <p>Discover tax-efficient strategies for passing assets to the next generation and maximizing your charitable giving.</p>
    </article>

    <aside class="raffle">
      <p class="win">WIN</p>
      <p class="amount">$500</p>
      <p class="prize">off an Estate Plan Package!</p>
    </aside>

    <div class="food">
      <svg width="116" height="92" viewBox="0 0 116 92" aria-hidden="true">
        <circle cx="58" cy="8" r="5" fill="none" stroke="#fff" stroke-width="4"/>
        <path d="M6 74 A52 52 0 0 1 110 74 Z" fill="none" stroke="#fff" stroke-width="5" stroke-linejoin="round"/>
        <line x1="2" y1="86" x2="114" y2="86" stroke="#fff" stroke-width="5" stroke-linecap="round"/>
      </svg>
      <p>Food will<br>be provided</p>
    </div>
  </section>

  <div class="venue-bar"></div>
  <div class="venue">
    <h4>Conference Hall</h4>
    <p>123 Anywhere St.,<br>Any City</p>
  </div>

  <div class="partner partner-law"><span>PWR Law</span><span class="mark"></span></div>
  <div class="partner partner-finance"><span class="mark"></span><span>Quelmora</span></div>
</main>
</body>
</html>
```